BrightPath Dental
Web Presence
BrightPath Dental - Information Technology
Creative Brief
Information Technology
www.brightpathdental-demo.com
Brightpath Dental provides a wide variety of high tech dental solutions at a competitive price. We pride ourselves on the extremely high level and speed of service that we provide to our clientele. We are a local computer company that specializes in bringing our clientele the best dental technology solutions available. By allowing us to correctly integrate the right dental technology solutions, it gives your practice a technological competitive edge, increases production, and significantly enhances your patient’s experience. We provide a full array of computer services for both small and large practices. Our team services PC's and networks, digital x-ray / imaging equipment, we also provide software & hardware sales, service, upgrades, and installations, as well as data storage and backup solutions. We also provide ongoing technical support to keep you comfortable with changing technologies and ensure your practice productivity.
would like CMS designed website for either joomla or wordpress. We need the wording and the design -- we are a Lumoverde Reseller and Installer so please check out their site listed below. our logo is available: http://orders.markcraftstudio-demo.com/contests/business-logo-brightpathdental
left side
http://www.lumoverdedental-demo.com/us_region/index.aspx
http://www.qwbadvisors-demo.com/articles
http://www.orb-sys-demo.com/index.html
Additional Sites that do similar work: http://www.mnzerodental-demo.com/dataprotection.htm http://www.fenwro-demo.com/customer_care.html http://www.glimvo-demo.com/ http://www.mnzerodental-demo.com/dataprotection.htm

```html
<!DOCTYPE html>
<html lang="en">
<head>
<meta charset="utf-8">
<title>BrightPath Dental</title>
<link href="https://fonts.googleapis.com/css2?family=Arimo:wght@400;700&family=PT+Serif:wght@400;700&display=swap" rel="stylesheet">
<style>
:root{
  --page:#ffffff;
  --navy:#0a3d7a;
  --blue:#1466b8;
  --blue-dark:#0b4f96;
  --blue-light:#3d8fdb;
  --red:#c0121a;
  --red-dark:#8e0a10;
  --text:#555a60;
  --muted:#8a9097;
  --footer:#2b2b2b;
  --footer-dark:#1c1c1c;
  --footer-text:#b9b9b9;
  --white:#ffffff;
}
*{box-sizing:border-box;margin:0;padding:0}
html,body{width:1200px;height:1099px;overflow:hidden;background:var(--page)}
body{font-family:"Arimo",Arial,sans-serif;color:var(--text);position:relative}
a{color:inherit;text-decoration:none}

.site-header{position:absolute;left:171px;top:0;width:864px;height:96px}
.brand{position:absolute;left:10px;top:26px;display:flex;align-items:center;gap:10px}
.brand-dot{width:34px;height:34px;border-radius:50%;background:var(--red)}
.brand-name{font-family:"PT Serif",Georgia,serif;font-weight:700;font-size:28px;color:var(--navy)}
.contact-line{position:absolute;right:6px;top:78px;font-size:10px;color:var(--muted)}

.main-nav{position:absolute;left:171px;top:99px;width:864px;height:36px;border-radius:6px 6px 0 0;
  background:linear-gradient(var(--blue-light),var(--blue-dark));display:flex;padding-left:18px}
.main-nav a{color:var(--white);font-size:12px;line-height:36px;padding:0 18px;border-right:1px solid rgba(255,255,255,.25)}
.dropdown{position:absolute;left:264px;top:135px;width:126px;background:var(--red);padding:6px 0;z-index:3;border:1px solid var(--red-dark)}
.dropdown a{display:block;color:var(--white);font-size:10px;padding:5px 12px;border-bottom:1px solid rgba(255,255,255,.2)}

.hero{position:absolute;left:171px;top:142px;width:864px;height:412px;overflow:hidden;border:1px solid #d6dde4}
.hero-photo{position:absolute;inset:0;background:
  radial-gradient(ellipse at 30% 20%,#f4f6f7 0%,rgba(244,246,247,0) 45%),
  radial-gradient(ellipse at 75% 55%,#9fb6c6 0%,rgba(159,182,198,0) 55%),
  linear-gradient(135deg,#c3ced6 0%,#e6ebee 45%,#a9bccb 100%)}
.hero-caption{position:absolute;left:0;top:246px;width:560px;height:150px;background:rgba(255,255,255,.88);padding:14px 18px}
.hero-caption h1{font-family:"PT Serif",Georgia,serif;font-weight:400;font-size:30px;line-height:34px;color:var(--blue)}
.hero-caption p{font-size:11px;line-height:14px;margin-top:8px;color:var(--text)}
.hero-arrow{position:absolute;top:190px;width:24px;height:34px;background:rgba(0,0,0,.35);display:flex;align-items:center;justify-content:center}
.hero-arrow.prev{left:0}.hero-arrow.next{right:0}
.hero-dots{position:absolute;right:48px;bottom:34px;display:flex;gap:10px}
.hero-dots span{width:12px;height:12px;border-radius:50%;background:rgba(255,255,255,.75)}
.hero-dots span.active{background:var(--blue)}

.features{position:absolute;left:171px;top:562px;width:864px;display:flex;gap:15px}
.feature{width:278px}
.feature-bar{height:34px;background:linear-gradient(var(--blue-light),var(--blue-dark));color:var(--white);
  font-family:"PT Serif",Georgia,serif;font-size:17px;line-height:34px;padding-left:12px;border-radius:4px 4px 0 0}
.feature-photo{height:88px}
.photo-system{background:linear-gradient(160deg,#5d9bd0 0%,#cfe1ef 60%,#7fa9c8 100%)}
.photo-ortho{background:linear-gradient(160deg,#e9d3c6 0%,#f6efe9 50%,#b9d3e6 100%)}
.photo-surgeons{background:linear-gradient(160deg,#d9e6ee 0%,#9fc1d8 55%,#eef3f6 100%)}
.feature h3{font-size:10px;font-weight:700;color:var(--blue-dark);margin-top:10px}
.feature p{font-size:9px;line-height:12px;margin-top:5px;color:var(--muted)}
.more{display:inline-block;margin-top:8px;background:var(--blue);color:var(--white);font-size:9px;padding:3px 8px;border-radius:2px}

.site-footer{position:absolute;left:0;top:800px;width:1200px;height:262px;background:linear-gradient(var(--footer),var(--footer-dark))}
.footer-cols{position:absolute;left:171px;top:50px;width:864px;display:flex;gap:24px}
.footer-col{width:198px}
.footer-col h2{font-family:"PT Serif",Georgia,serif;font-weight:400;font-size:22px;color:var(--white);display:flex;align-items:center;gap:10px}
.footer-col h2 svg{flex:none}
.footer-col strong{display:block;font-size:9px;color:var(--white);margin-top:14px}
.footer-col p{font-size:9px;line-height:13px;color:var(--footer-text);margin-top:6px}
.copyright{position:absolute;left:0;bottom:8px;width:100%;text-align:center;font-size:9px;color:var(--muted)}
.bottom-nav{position:absolute;left:0;top:1062px;width:1200px;height:37px;background:linear-gradient(var(--red),var(--red-dark));
  display:flex;justify-content:center;gap:44px}
.bottom-nav a{color:var(--white);font-size:11px;line-height:37px}
</style>
</head>
<body>
<header class="site-header">
  <div class="brand"><span class="brand-dot"></span><span class="brand-name">BrightPath Dental</span></div>
  <div class="contact-line">Call Us: 0800 000 000 &nbsp;|&nbsp; Mail: info@brightpathdental-demo.com</div>
</header>

<nav class="main-nav">
  <a href="#">Home</a><a href="#">Specialites</a><a href="#">Dental System</a><a href="#">Our Partners</a><a href="#">Careers</a><a href="#">Contact Us</a>
</nav>
<div class="dropdown">
  <a href="#">Orthodontics</a><a href="#">Endodontics</a><a href="#">Periodontics</a><a href="#">Oral Surgery</a>
</div>

<section class="hero">
  <div class="hero-photo" role="img" aria-label="Dental team examining an x-ray in a treatment room"></div>
  <div class="hero-caption">
    <h1>BrightPath The Dental<br>InformationTechnology Company</h1>
    <p>Brightpath Dental provides a wide variety of high tech dental solutions at a competitive price. We pride ourselves on the extremely high level and speed of service that we provide to our clientele.</p>
  </div>
  <div class="hero-arrow prev"><svg width="10" height="14"><path d="M8 1 2 7l6 6" fill="none" stroke="#fff" stroke-width="2"/></svg></div>
  <div class="hero-arrow next"><svg width="10" height="14"><path d="M2 1l6 6-6 6" fill="none" stroke="#fff" stroke-width="2"/></svg></div>
  <div class="hero-dots"><span class="active"></span><span></span><span></span><span></span><span></span></div>
</section>

<section class="features">
  <article class="feature">
    <div class="feature-bar">Dental System</div>
    <div class="feature-photo photo-system" role="img" aria-label="Dental treatment chair and equipment"></div>
    <h3>Orthodontists, CFSS and Endodontic Systems</h3>
    <p>Our team installs digital x-ray and imaging systems, manages practice software and networks, and keeps every chair connected so your clinic runs smoothly each day.</p>
    <a class="more" href="#">More</a>
  </article>
  <article class="feature">
    <div class="feature-bar">Orthodontists</div>
    <div class="feature-photo photo-ortho" role="img" aria-label="Patient receiving orthodontic care"></div>
    <h3>Orthodontists, CFSS and Endodontic Systems</h3>
    <p>Our team installs digital x-ray and imaging systems, manages practice software and networks, and keeps every chair connected so your clinic runs smoothly each day.</p>
    <a class="more" href="#">More</a>
  </article>
  <article class="feature">
    <div class="feature-bar">Sergeons</div>
    <div class="feature-photo photo-surgeons" role="img" aria-label="Dental surgeons at work"></div>
    <h3>Orthodontists, CFSS and Endodontic Systems</h3>
    <p>Our team installs digital x-ray and imaging systems, manages practice software and networks, and keeps every chair connected so your clinic runs smoothly each day.</p>
    <a class="more" href="#">More</a>
  </article>
</section>

<footer class="site-footer">
  <div class="footer-cols">
    <div class="footer-col">
      <h2><svg width="22" height="22"><path d="M11 2l2.6 6 6.4.5-4.9 4.2 1.5 6.3L11 15.6 5.4 19l1.5-6.3L2 8.5 8.4 8z" fill="#fff"/></svg>Specialites</h2>
      <strong>Orthodontists, CFSS and Endodontic Systems</strong>
      <p>We design, install and support complete dental IT setups, from imaging sensors to secure backups, for small and large practices alike.</p>
    </div>
    <div class="footer-col">
      <h2><svg width="22" height="22"><circle cx="11" cy="11" r="8" fill="none" stroke="#fff" stroke-width="2"/><circle cx="11" cy="11" r="3" fill="#fff"/></svg>Dental System</h2>
      <strong>We are among the leaders in dental technology</strong>
      <p>Our systems bring faster charting, clear imaging and reliable storage, giving your practice a real competitive edge.</p>
    </div>
    <div class="footer-col">
      <h2><svg width="22" height="22"><rect x="3" y="4" width="16" height="14" fill="none" stroke="#fff" stroke-width="2"/><path d="M6 9h10M6 13h10" stroke="#fff" stroke-width="1.5"/></svg>News</h2>
      <strong>New imaging suite now available</strong>
      <p>Read about our latest upgrades and training sessions for local clinics this season.</p>
      <p>We are proud to support every client with quick, friendly service.</p>
    </div>
    <div class="footer-col">
      <h2><svg width="22" height="22"><rect x="2" y="5" width="18" height="12" fill="none" stroke="#fff" stroke-width="2"/><path d="M2 5l9 7 9-7" fill="none" stroke="#fff" stroke-width="2"/></svg>Contact Us</h2>
      <strong>Call Us: 0800 000 000</strong>
      <p>Mail: info@brightpathdental-demo.com</p>
      <p>Our support team answers questions on hardware, software, imaging and backups every working day.</p>
    </div>
  </div>
  <div class="copyright">Copyright © 2011 BrightPath Dental. All rights reserved.</div>
</footer>

<nav class="bottom-nav">
  <a href="#">Home</a><a href="#">Specialites</a><a href="#">Dental System</a><a href="#">Our Partners</a><a href="#">Careers</a><a href="#">Contact Us</a>
</nav>
</body>
</html>
```